依頼詳細
押してみたくなる、素敵なバナーが出来上がることを期待しております。
記載項目
大きいサイズのバナーの方ですが、ロゴを入れることになった場合は
後からデータをお渡しします。
サイズ
• 60×150 4kb以下  300×300 1200×628 3mb以下
希望イメージ
シンプル 複雑
単色 カラフル
暗い 明るい
日常 高級
遊び心 厳粛
未来的 伝統的
女性的 男性的
希望する色
青系、水色系
納品ファイル
• 高解像度JPG (.jpg)
• イラストレーター形式 (.ai)
• PNG形式 (.png)
補足説明
■ 選んだ理由

当社のイメージする部分とデザインの雰囲気があっていましたので選ばせて頂きました。

■ 提案者全員のお礼・コメント

とてもきれいなデザインが多くて選定するのに時間がかかってしまうほどでした。

有難う御座いました。

```html
<!DOCTYPE html>
<html lang="ja">
<head>
<meta charset="UTF-8">
<title>理想のお相手探します。｜安心できる婚活</title>
<link href="https://fonts.googleapis.com/css2?family=Noto+Serif+JP:wght@700;900&display=swap" rel="stylesheet">
<style>
  :root {
    --sky-blue: #6c9fd0;
    --band-blue: #5e91c7;
    --frame-blue: #5a8cc2;
    --paper: #fdfdfd;
    --accent-red: #c3162e;
    --white: #ffffff;
  }
  html, body {
    margin: 0;
    padding: 0;
    width: 1200px;
    height: 3000px;
    overflow: hidden;
    background: var(--white);
  }
  .banner {
    position: relative;
    width: 1200px;
    height: 3000px;
    box-sizing: border-box;
    border-left: 10px solid var(--frame-blue);
    border-right: 10px solid var(--frame-blue);
    font-family: "Noto Serif JP", serif;
    overflow: hidden;
  }
  .hero {
    position: absolute;
    left: 0; top: 0;
    width: 100%;
    height: 1860px;
    background: var(--sky-blue);
  }
  .headline-column {
    position: absolute;
    top: 40px;
    writing-mode: vertical-rl;
    color: var(--white);
    font-weight: 900;
    font-size: 216px;
    line-height: 1;
    margin: 0;
  }
  .headline-main {
    left: 630px;
    letter-spacing: 80px;
  }
  .headline-sub {
    left: 280px;
    letter-spacing: 26px;
  }
  .message {
    position: absolute;
    left: 0; top: 1860px;
    width: 100%;
    height: 1000px;
    background: var(--paper);
    text-align: center;
    color: var(--accent-red);
    font-weight: 700;
  }
  .message-line {
    display: block;
    font-size: 216px;
    line-height: 1;
    margin: 0;
    letter-spacing: -4px;
  }
  .message-line.first { padding-top: 180px; }
  .message-line.second { padding-top: 50px; }
  .brand-band {
    position: absolute;
    left: 0; bottom: 0;
    width: 100%;
    height: 140px;
    background: var(--band-blue);
    display: flex;
    align-items: center;
    justify-content: center;
  }
  .brand-name {
    color: var(--white);
    font-weight: 900;
    font-size: 112px;
    letter-spacing: 2px;
    line-height: 1;
  }
</style>
</head>
<body>
  <div class="banner">
    <section class="hero">
      <h1 class="headline-column headline-main">理想のお相手</h1>
      <p class="headline-column headline-sub">探します。</p>
    </section>
    <section class="message">
      <p class="message-line first">安心できる</p>
      <p class="message-line second">婚活</p>
    </section>
    <footer class="brand-band">
      <span class="brand-name">AOBA BRIDAL</span>
    </footer>
  </div>
</body>
</html>
```